Book cover Design for her new book called 'Walking a path lined with courage and grace'

My name is Velorashi, I am the founder of The Quiet Lantern.
http://velorashi-wren.examplestore.com/
My book is an inspirational story of love and triumphing from adversity. After 40 years of surviving a life full of sexual abuse, physical and mental abuse and living with the effects of poor self-esteem and post traumatic stress disorder, this book is a guide to help others navigate away from negative emotions and help them find their own light in life. With the techniques developed and described in the book The Quiet Lantern's mission is to empower people with the journey to their own hearts and create warmth, love and inspiration.
The colours in the website represent the softness that I love and I prefer flowers. The colour also can be soft as well as vibrant and feminine. The final design should represent healing, love, inspiration and passion.

Target Market(s)

Women over the age of 25 -80
Teenagers suffering from depression
Men and women suffering from poor self esteem
Woman who have poor self confidence.

Requirements
Should not have
• Should not be dark in colour or imagery.

```html
<!DOCTYPE html>
<html lang="en">
<head>
<meta charset="UTF-8">
<title>Walking a Path Lined with Courage and Grace — Book Cover</title>
<link rel="stylesheet" href="https://fonts.googleapis.com/css2?family=Source+Sans+3:wght@400;500&display=swap">
<style>
  :root {
    --page-bg: #ffffff;
    --rose: #e97fa6;
    --orchid: #c59ac9;
    --plum: #5f2a72;
    --sky: #6cc3ea;
    --cobalt: #3f5fb0;
    --lilac: #b9a3d6;
    --ink-light: #ffffff;
    --shadow-soft: rgba(70, 20, 80, 0.55);
    --lily-white: #f4f1f3;
    --stem-green: #7a8f3a;
  }

  * { box-sizing: border-box; margin: 0; padding: 0; }

  html, body {
    width: 1200px;
    height: 1000px;
    overflow: hidden;
    background: var(--page-bg);
  }

  .canvas {
    position: relative;
    width: 1200px;
    height: 1000px;
  }

  .book-cover {
    position: absolute;
    left: 350px;
    top: 112px;
    width: 500px;
    height: 776px;
    overflow: hidden;
    background:
      radial-gradient(circle at 8% 8%, var(--rose) 0, transparent 28%),
      radial-gradient(circle at 80% 8%, var(--rose) 0, transparent 26%),
      radial-gradient(circle at 85% 30%, var(--plum) 0, transparent 25%),
      radial-gradient(circle at 55% 40%, var(--sky) 0, transparent 22%),
      radial-gradient(circle at 15% 42%, var(--plum) 0, transparent 24%),
      radial-gradient(circle at 15% 65%, var(--rose) 0, transparent 22%),
      radial-gradient(circle at 52% 72%, var(--rose) 0, transparent 24%),
      radial-gradient(circle at 90% 70%, var(--orchid) 0, transparent 26%),
      radial-gradient(circle at 10% 88%, var(--cobalt) 0, transparent 22%),
      radial-gradient(circle at 90% 95%, var(--cobalt) 0, transparent 25%),
      radial-gradient(circle at 45% 100%, var(--sky) 0, transparent 28%),
      var(--lilac);
  }

  .book-title {
    position: absolute;
    left: 34px;
    top: 48px;
    width: 450px;
    font-family: "Source Sans 3", sans-serif;
    font-weight: 400;
    font-size: 44px;
    line-height: 1.08;
    letter-spacing: 0.2px;
    text-transform: uppercase;
    color: var(--ink-light);
    text-shadow: 0 2px 10px var(--shadow-soft);
  }

  .lily-illustration {
    position: absolute;
    left: 0;
    top: 240px;
    width: 270px;
    height: 536px;
    border-radius: 0 60% 0 0;
    background: linear-gradient(160deg, var(--lily-white) 0%, rgba(244,241,243,0.6) 35%, var(--stem-green) 75%, rgba(122,143,58,0.7) 100%);
    opacity: 0.85;
  }

  .book-author {
    position: absolute;
    left: 0;
    right: 0;
    top: 697px;
    text-align: center;
    padding-left: 50px;
    font-family: "Source Sans 3", sans-serif;
    font-weight: 400;
    font-size: 40px;
    color: var(--ink-light);
    text-shadow: 0 2px 10px var(--shadow-soft);
  }
</style>
</head>
<body>
  <main class="canvas">
    <section class="book-cover">
      <h1 class="book-title">Walking a path<br>lined with courage<br>and grace</h1>
      <div class="lily-illustration" role="img" aria-label="Illustration of two white calla lilies on long green stems with a leaf"></div>
      <p class="book-author">Velorashi Wren</p>
    </section>
  </main>
</body>
</html>
```